Redesign Website - Current one too plain

The description is in the uploaded file. Please let me know if you need any more information. I'd prefer it if someone could implement the design to a WordPress site but the best design will win, regardless.
I would like the forms to look nice as well
UPDATE:
I don't think we can use the images that I provided, I think they make the site look a bit 'cheap' and I really don't know how to replace them. One thought I have had is to make the "Simple, Unique, Effective" a second feature on the right side of the page with the search on the left
Target Market(s)
Small companies, private sellers of cars and people who rent their caravan/holiday home out
Industry/Entity Type
Advertising
Number of Pages Required
3 page
Colors
Designer to choose colors to be used in the design.
Look and feel

```html
<!DOCTYPE html>
<html lang="en">
<head>
<meta charset="utf-8">
<title>VANTO – Discover And Connect</title>
<link href="https://fonts.googleapis.com/css2?family=Inter:wght@400;500;600;700&display=swap" rel="stylesheet">
<style>
  :root {
    --ink-dark: #242424;
    --lime: #e8fb52;
    --white: #ffffff;
    --black: #000000;
  }
  * { margin: 0; padding: 0; box-sizing: border-box; }
  html, body { width: 754px; height: 1200px; overflow: hidden; }
  body {
    position: relative;
    background: var(--ink-dark);
    font-family: "Inter", Arial, sans-serif;
    color: var(--white);
  }
  .abs { position: absolute; }

  /* Header */
  .brand {
    left: 53px; top: 22px; display: flex; align-items: center; gap: 6px;
    color: var(--lime); font-size: 14px; font-weight: 500; letter-spacing: 0.5px;
  }
  .brand-dot { width: 18px; height: 18px; border-radius: 50%; background: var(--lime); }
  .main-nav { top: 26px; font-size: 8.5px; font-weight: 500; }
  .main-nav a { position: absolute; color: var(--white); text-decoration: none; white-space: nowrap; }
  .btn {
    display: flex; align-items: center; justify-content: center;
    background: var(--lime); color: var(--ink-dark); border-radius: 12px; font-weight: 500;
  }
  .btn-login { left: 614px; top: 22px; width: 87px; height: 23px; font-size: 11px; }

  /* Hero */
  .hero-title {
    left: 0; width: 754px; top: 112px; text-align: center;
    font-size: 38px; font-weight: 600; letter-spacing: 0.3px;
  }
  .hero-sub { left: 0; width: 754px; top: 169px; text-align: center; font-size: 10.5px; font-weight: 500; }
  .code-char {
    top: 220px; width: 40px; text-align: center; color: var(--lime);
    font-size: 46px; font-weight: 600; line-height: 56px;
  }
  .chevron { width: 11px; height: 11px; }
  .chip {
    top: 316px; height: 21px; border: 1px solid var(--lime); border-radius: 11px;
    color: var(--lime); font-size: 10.5px; display: flex; align-items: center; justify-content: center;
  }
  .btn-search { left: 302px; top: 366px; width: 150px; height: 23px; font-size: 10.5px; font-weight: 400; }

  /* Benefits */
  .benefits {
    left: 36px; top: 457px; width: 683px; height: 384px;
    background: var(--lime); border-radius: 20px; color: var(--black);
  }
  .section-title { position: absolute; left: 0; width: 100%; text-align: center; font-size: 16.5px; font-weight: 600; }
  .benefit-icon {
    position: absolute; top: 87px; width: 71px; height: 71px; background: var(--black); border-radius: 11px;
    display: flex; align-items: center; justify-content: center;
  }
  .benefit-label { position: absolute; top: 165px; font-size: 13px; font-weight: 700; line-height: 23px; }
  .benefit-copy { position: absolute; left: 28px; font-size: 10.2px; white-space: nowrap; }
  .benefit-copy b { font-weight: 700; }

  /* About */
  .about {
    left: 36px; top: 879px; width: 683px; height: 302px; background: var(--white); border-radius: 20px; color: var(--black);
  }
  .about-card {
    position: absolute; top: 96px; width: 168px; height: 167px; background: var(--ink-dark);
    border-radius: 18px; text-align: center;
  }
  .about-card svg { position: absolute; left: 59px; top: 32px; }
  .about-card h3 { position: absolute; left: 0; width: 100%; top: 96px; color: var(--lime); font-size: 13px; font-weight: 500; }
  .about-card p { position: absolute; left: 16px; right: 16px; top: 116px; color: var(--white); font-size: 8.4px; line-height: 10px; }
</style>
</head>
<body>
  <header>
    <div class="abs brand"><span class="brand-dot"></span>VANTO</div>
    <nav class="abs main-nav">
      <a href="#" style="left:257px">Home</a>
      <a href="#" style="left:305px">Advertise</a>
      <a href="#" style="left:372px">Contact</a>
      <a href="#" style="left:438px">Register</a>
    </nav>
    <a class="abs btn btn-login">Login</a>
  </header>

  <section class="hero">
    <h1 class="abs hero-title">Discover And Connect</h1>
    <p class="abs hero-sub">Display Your Unique Code on Your Vehicle to Attract Customers</p>

    <svg class="abs chevron" style="left:345px;top:212px" viewBox="0 0 12 12"><circle cx="6" cy="6" r="6" fill="#e8fb52"/><path d="M3.5 7.2 6 4.8 8.5 7.2" stroke="#242424" stroke-width="1.3" fill="none"/></svg>
    <svg class="abs chevron" style="left:398px;top:212px" viewBox="0 0 12 12"><circle cx="6" cy="6" r="6" fill="#e8fb52"/><path d="M3.5 7.2 6 4.8 8.5 7.2" stroke="#242424" stroke-width="1.3" fill="none"/></svg>
    <div class="abs code-char" style="left:330px">S</div>
    <div class="abs code-char" style="left:383px">6</div>
    <svg class="abs chevron" style="left:345px;top:276px" viewBox="0 0 12 12"><circle cx="6" cy="6" r="6" fill="#e8fb52"/><path d="M3.5 4.8 6 7.2 8.5 4.8" stroke="#242424" stroke-width="1.3" fill="none"/></svg>
    <svg class="abs chevron" style="left:398px;top:276px" viewBox="0 0 12 12"><circle cx="6" cy="6" r="6" fill="#e8fb52"/><path d="M3.5 4.8 6 7.2 8.5 4.8" stroke="#242424" stroke-width="1.3" fill="none"/></svg>

    <div class="abs chip" style="left:276px;width:34px">Car</div>
    <div class="abs chip" style="left:332px;width:59px">Caravan</div>
    <div class="abs chip" style="left:413px;width:65px">Company</div>

    <a class="abs btn btn-search">Search</a>
  </section>

  <section class="abs benefits">
    <h2 class="section-title" style="top:30px">Benefits of Advertising with us</h2>

    <div class="benefit-icon" style="left:134px">
      <svg width="46" height="46" viewBox="0 0 46 46" fill="none" stroke="#fff" stroke-width="1.6">
        <circle cx="23" cy="23" r="15"/><circle cx="23" cy="23" r="11"/>
        <path d="M23 4v6M23 36v6M4 23h6M36 23h6"/>
        <circle cx="23" cy="19" r="3"/><circle cx="17" cy="21" r="2.4"/><circle cx="29" cy="21" r="2.4"/>
        <path d="M17 30c0-4 3-6 6-6s6 2 6 6M12.5 28c0-3 2-4.5 4.5-4.5M33.5 28c0-3-2-4.5-4.5-4.5"/>
      </svg>
    </div>
    <div class="benefit-label" style="left:134px">Targeted<br>Exposure</div>

    <div class="benefit-icon" style="left:305px">
      <svg width="50" height="46" viewBox="0 0 50 46" fill="none" stroke="#fff" stroke-width="1.8">
        <path d="M6 28c6-8 12-11 19-11s13 3 19 11c-6 8-12 11-19 11S12 36 6 28z"/>
        <circle cx="25" cy="28" r="6"/><circle cx="25" cy="28" r="2.5"/>
        <path d="M25 4v8M17 6l2 7M33 6l-2 7M10 11l4 5M40 11l-4 5M4 19l5 2M46 19l-5 2"/>
      </svg>
    </div>
    <div class="benefit-label" style="left:306px">Increased<br>&nbsp;&nbsp;Visibility</div>

    <div class="benefit-icon" style="left:477px">
      <svg width="46" height="46" viewBox="0 0 46 46" fill="none" stroke="#fff" stroke-width="1.6">
        <path d="M20 8h8l-2 5h-4z"/><path d="M22 13c-7 3-10 9-9 15 1 4 4 6 10 6s10-2 11-6c1-6-3-12-10-15"/>
        <path d="M26 19c-1-1-5-1-5 1.5s5 1.5 5 4-4 2.5-5 1M23.5 17v12"/>
        <path d="M6 30h6l6 3h6a2 2 0 0 1 0 4h-7M6 39h18l10-4"/>
      </svg>
    </div>
    <div class="benefit-label" style="left:477px;text-align:center;width:72px">Flexible<br>Ad Options</div>

    <p class="benefit-copy" style="top:247px"><b>Targeted Exposure:</b> Reach your desired audience directly, ensuring maximum impact for your advertising efforts.</p>
    <p class="benefit-copy" style="top:283px"><b>Increased Visibility:</b> Gain prominence on our website, increasing your brand recognition and customer engagement.</p>
    <p class="benefit-copy" style="top:319px"><b>Flexible Ad Options:</b> Choose from a variety of advertising formats and durations that suit your budget and marketing goals.</p>
  </section>

  <section class="abs about">
    <h2 class="section-title" style="top:38px">About us</h2>

    <div class="about-card" style="left:48px">
      <svg width="50" height="50" viewBox="0 0 50 50" fill="none" stroke="#e8fb52" stroke-width="1.6" stroke-linecap="round" stroke-linejoin="round">
        <path d="M14 4v4M8 7l2 3M20 7l-2 3"/>
        <path d="M14 48v-6c-3-3-4-7-4-11V20c0-2 3-2 4 0l1 3 5-6c2-2 4 0 3 2l-3 5 8-11c2-2 5 0 4 3l-4 9c2 6 1 12-4 17v6"/>
        <path d="M11 24h8M11 30h9M12 36h8"/>
      </svg>
      <h3>Simple</h3>
      <p>Create your advert and display your code</p>
    </div>

    <div class="about-card" style="left:257px">
      <svg width="50" height="50" viewBox="0 0 50 50" fill="none" stroke="#e8fb52" stroke-width="1.6" stroke-linecap="round">
        <path d="M8 28c-2-10 3-20 13-21 8-1 15 5 15 13"/>
        <path d="M13 30c-1-7 2-14 8-15s11 3 11 8"/>
        <path d="M18 32c-1-5 0-10 4-10s6 3 6 5"/>
        <circle cx="30" cy="32" r="8"/><path d="M36 38l8 8"/>
      </svg>
      <h3>Unique</h3>
      <p>Customers find you by an easy-to-remember code</p>
    </div>

    <div class="about-card" style="left:467px">
      <svg width="50" height="50" viewBox="0 0 50 50" fill="none" stroke="#e8fb52" stroke-width="1.6" stroke-linecap="round" stroke-linejoin="round">
        <path d="M41 12A22 22 0 0 0 5 20M9 38a22 22 0 0 0 36-8"/>
        <path d="M37 8l4 4-5 2M13 42l-4-4 5-2"/>
        <circle cx="25" cy="25" r="11"/><circle cx="25" cy="25" r="7"/>
        <path d="M25 21v4l3 2"/>
      </svg>
      <h3>Effective</h3>
      <p>Customers are directed to you and not a list of your competitors</p>
    </div>
  </section>
</body>
</html>
```